Need a book cover design for a Lumora Book on Herbal Remedies

I need a book cover for my new ebook, here are the details:
Title: Meadow Cures
Sub-Heading: Buried Ancient Garden Tonics
Reclaiming the Wisdom of Roots for Everyday Wellness and Strength
Author: Nora Belcourt

```html
<!DOCTYPE html>
<html lang="en">
<head>
<meta charset="utf-8">
<title>Meadow Cures — Nora Belcourt</title>
<link rel="stylesheet" href="https://fonts.googleapis.com/css2?family=Bebas+Neue&family=Oswald:wght@500&family=Montserrat:wght@300&display=swap">
<style>
  :root {
    --page: #ffffff;
    --green-top: #2c6531;
    --green-upper: #3b7a37;
    --green-mid: #5c9a42;
    --green-low: #86bb50;
    --green-bottom: #a3d05e;
    --title-yellow: #f6ee1a;
    --text-white: #ffffff;
    --author-ink: #141810;
  }
  * { margin: 0; padding: 0; box-sizing: border-box; }
  html, body {
    width: 838px;
    height: 1200px;
    overflow: hidden;
    background: var(--page);
  }
  .cover {
    position: absolute;
    left: 48px;
    top: 48px;
    width: 738px;
    height: 1106px;
    overflow: hidden;
  }
  .cover__photo {
    position: absolute;
    inset: 0;
    background:
      radial-gradient(ellipse 520px 380px at 50% 0%, rgba(20, 50, 24, 0.35) 0%, transparent 100%),
      linear-gradient(180deg,
        var(--green-top) 0%,
        var(--green-upper) 30%,
        var(--green-mid) 55%,
        var(--green-low) 78%,
        var(--green-bottom) 100%);
  }
  .cover__title {
    position: absolute;
    left: 0;
    right: 0;
    top: 228px;
    text-align: center;
    font-family: "Bebas Neue", "Oswald", sans-serif;
    font-size: 145px;
    line-height: 120px;
    letter-spacing: 4px;
    color: var(--title-yellow);
    text-shadow: 0 4px 10px rgba(0, 0, 0, 0.35);
  }
  .cover__subtitle {
    position: absolute;
    left: 0;
    right: 0;
    top: 469px;
    text-align: center;
    font-family: "Oswald", sans-serif;
    font-weight: 500;
    font-size: 29px;
    letter-spacing: 0.5px;
    color: var(--text-white);
    text-transform: uppercase;
  }
  .cover__tagline {
    position: absolute;
    left: 0;
    right: 0;
    top: 572px;
    text-align: center;
    font-family: "Montserrat", sans-serif;
    font-weight: 300;
    font-size: 24px;
    line-height: 43px;
    letter-spacing: 2px;
    color: var(--text-white);
    text-transform: uppercase;
  }
  .cover__author {
    position: absolute;
    left: 0;
    right: 0;
    top: 955px;
    text-align: center;
    font-family: "Montserrat", sans-serif;
    font-weight: 300;
    font-size: 38px;
    letter-spacing: 6px;
    color: var(--author-ink);
    text-transform: uppercase;
  }
</style>
</head>
<body>
  <main class="cover">
    <div class="cover__photo" role="img" aria-label="Overhead photo of loose green tea leaves in a wooden bowl, a cup of green tea on a dark saucer and fresh tea leaf sprigs on a green textured surface"></div>
    <h1 class="cover__title">Meadow<br>Cures</h1>
    <p class="cover__subtitle">Buried Ancient Garden Tonics</p>
    <p class="cover__tagline">Reclaiming the wisdom<br>of roots for everyday<br>wellness and strength</p>
    <p class="cover__author">Nora Belcourt</p>
  </main>
</body>
</html>
```